Artificial intelligence, machine learning, and automation company needs a sexy business card design

We need a sleek and sexy business card design for an AI consulting company based in Philadelphia PA. We provide custom machine learning and automation solutions for companies of all shapes and sizes. The primary industries that we serve are pharmaceuticals, engineering, healthcare, and computer software. We would like the designs to be a black business card that uses green as a sleek accent color. The final design should communicate intelligence, cutting edge new-tech, and optimization.

Target Market(s)

C-level and VP level executives of multi-million annual companies. Mostly in Pharma, Healthcare, Real Estate, Retail, and Engineering

Industry/Entity Type

Computer Software

Contact Information for Business Card

Name: Jack Moss
Title: CEO
Cell: 215 604 8293
Email: JackM@quillarcworks.example
Website: www.QuillarcWorks.example

Font styles to use
Sans Serif

Colors

Designer to choose colors to be used in the design.

Requirements
Must have
• 1) Attached Quillarc Logo (either with colors or not/embossed)
• 2) "Artificial Intelligence" "Automation" and "Machine Learning"
• 3) "Quillarc Laboratories" or "Quillarc Works" or "Quillarc"
• 4) Sexy AF.
Nice to have
• Black card / dark card color, "Quillarc Green" accent colors (in attached .ai file), Embossment of logo/name/etc, thick card stock, colored borders (on card sides, not front/back faces)
Should not have
• Should not be bland, or unsexy.

```html
<!DOCTYPE html>
<html lang="en">
<head>
<meta charset="utf-8">
<title>Quillarc Laboratories — Business Card</title>
<link rel="stylesheet" href="https://fonts.googleapis.com/css2?family=Bebas+Neue&family=Montserrat:wght@400&family=Open+Sans:wght@400&display=swap">
<style>
  :root {
    --backdrop: #5e4433;
    --card: #232323;
    --emboss: #8c8c8c;
    --accent: #4cc3a8;
    --text-light: #f2f2f2;
    --divider: #d9d9d9;
  }
  * { margin: 0; padding: 0; box-sizing: border-box; }
  html, body { width: 1200px; height: 1000px; overflow: hidden; }
  body { background: var(--backdrop); position: relative; }

  .card {
    position: absolute;
    left: 266px;
    width: 666px;
    height: 397px;
    background: var(--card);
    box-shadow: 0 4px 14px rgba(0,0,0,0.45);
  }
  .card--front { top: 74px; }
  .card--back { top: 533px; }

  /* Front: brand lockup */
  .brand {
    position: absolute;
    left: 141px;
    top: 152px;
    display: flex;
    align-items: center;
    gap: 20px;
  }
  .brand-mark {
    width: 96px;
    height: 94px;
    border: 3px solid var(--emboss);
  }
  .brand-name {
    font-family: 'Montserrat', sans-serif;
    font-weight: 400;
    color: var(--emboss);
    line-height: 1;
  }
  .brand-name-primary {
    display: block;
    font-size: 48px;
    letter-spacing: 4px;
  }
  .brand-name-secondary {
    display: block;
    margin-top: 10px;
    font-size: 22px;
    letter-spacing: 5.5px;
  }

  /* Back: contact block */
  .identity {
    position: absolute;
    right: 382px;
    top: 168px;
    text-align: right;
  }
  .person-name {
    font-family: 'Bebas Neue', sans-serif;
    font-size: 45px;
    line-height: 40px;
    color: var(--accent);
    letter-spacing: 0.5px;
  }
  .person-title {
    font-family: 'Open Sans', sans-serif;
    font-size: 15px;
    color: var(--text-light);
    margin-top: 2px;
  }
  .divider {
    position: absolute;
    left: 303px;
    top: 169px;
    width: 1.5px;
    height: 56px;
    background: var(--divider);
  }
  .contact-list {
    position: absolute;
    left: 324px;
    top: 166px;
    list-style: none;
    font-family: 'Open Sans', sans-serif;
    font-size: 15.5px;
    color: var(--text-light);
  }
  .contact-item {
    display: flex;
    align-items: center;
    gap: 6px;
    height: 20px;
  }
  .contact-icon { width: 14px; height: 14px; flex: none; }
</style>
</head>
<body>
  <section class="card card--front">
    <div class="brand">
      <div class="brand-mark"></div>
      <div class="brand-name">
        <span class="brand-name-primary">QUILLARC</span>
        <span class="brand-name-secondary">LABORATORIES</span>
      </div>
    </div>
  </section>

  <section class="card card--back">
    <div class="identity">
      <div class="person-name">JACK MOSS</div>
      <div class="person-title">CEO</div>
    </div>
    <div class="divider"></div>
    <ul class="contact-list">
      <li class="contact-item">
        <svg class="contact-icon" viewBox="0 0 16 16" fill="none" stroke="#4cc3a8" stroke-width="1.3">
          <path d="M3 1.5h3l1.3 3.3-1.8 1.2a8 8 0 0 0 4.5 4.5l1.2-1.8 3.3 1.3v3a1.5 1.5 0 0 1-1.6 1.5A12.5 12.5 0 0 1 1.5 3.1 1.5 1.5 0 0 1 3 1.5z"/>
        </svg>
        <span>215 604 8293</span>
      </li>
      <li class="contact-item">
        <svg class="contact-icon" viewBox="0 0 16 16" fill="none" stroke="#4cc3a8" stroke-width="1.3">
          <rect x="1.5" y="3.5" width="13" height="9"/>
          <path d="M1.5 3.5l6.5 5 6.5-5"/>
        </svg>
        <span>JackM@quillarcworks.example</span>
      </li>
      <li class="contact-item">
        <svg class="contact-icon" viewBox="0 0 16 16" fill="none" stroke="#4cc3a8" stroke-width="1.3">
          <circle cx="8" cy="8" r="6.5"/>
          <ellipse cx="8" cy="8" rx="2.8" ry="6.5"/>
          <path d="M1.5 8h13M2.5 4.8h11M2.5 11.2h11"/>
        </svg>
        <span>www.QuillarcWorks.example</span>
      </li>
    </ul>
  </section>
</body>
</html>
```